Interior Decorating business - Logo & Stationery

"Velvet Lantern" is a newly established interior decorating company, based in Sydney, providing interior decorating, colour consulting and property styling services to residential and commercial clients.

We require a logo and stationery design (double-sided business card, A4 letterhead and with compliments slip (210mm X 95mm))

Letterhead information and with compliments slip:
Address - 22/31-33 Thornbury Rd, Kelvin Grove NSW 2098
Phone - (02)9617 4280
Mobile - 0427 386 509
Email - maeve@velvetlantern.com.au
Web - www.velvetlantern.com.au
ABN - 47392815064

Business Cards should be double sided and are to include;
Maeve Hollis
Director

with email address, mobile number, website as listed above

They also need to include services offered i.e. Interior Decorating, Colour Consulting, Property Styling

Please note that the current content on the website will be updated, so disregard logo and content currently on the website.

Target Market(s)

Target market is two-fold - residential clients (primarily homeowners with pride in their homes) and commerical clients (specifically business owners of retail shops and cafes and property developers)

Industry/Entity Type

Residential

```html
<!DOCTYPE html>
<html lang="en">
<head>
<meta charset="utf-8">
<title>Velvet Lantern – Business Card Presentation</title>
<link href="https://fonts.googleapis.com/css2?family=Fredoka:wght@600&family=Roboto+Condensed:wght@700&family=Lobster&family=Tinos:wght@700&display=swap" rel="stylesheet">
<style>
  :root {
    --paper: #ffffff;
    --brick: #cf5a3c;
    --brick-dark: #b84a30;
    --leaf: #7aac3e;
    --leaf-dark: #5f8f34;
    --leaf-pale: #b7d0a4;
    --lemon: #f0e51f;
    --ink-blue: #2b3a9c;
    --cream: #f1efc8;
    --olive: #c2bd6a;
    --steel: #8f9496;
    --white: #ffffff;
    --service-green: #4f8a2a;
  }
  * { box-sizing: border-box; margin: 0; padding: 0; }
  html, body { width: 1196px; height: 1200px; overflow: hidden; background: var(--paper); }
  .canvas { position: relative; width: 1196px; height: 1200px; }

  .card { position: absolute; overflow: hidden; box-shadow: 0 2px 6px rgba(0,0,0,.25); }
  .card svg.bg { position: absolute; inset: 0; width: 100%; height: 100%; }

  .wordmark {
    position: absolute;
    font-family: "Fredoka", "Arial Rounded MT Bold", sans-serif;
    font-weight: 600;
    color: var(--lemon);
    line-height: .95;
    display: flex; align-items: center; gap: 14px;
  }
  .wordmark .dot { width: 22px; height: 22px; border-radius: 50%; background: currentColor; flex: none; }

  .services {
    position: absolute;
    font-family: "Roboto Condensed", "Arial Narrow", sans-serif;
    font-weight: 700;
    font-size: 17px;
    line-height: 1.4;
  }

  /* Card front – diamond pattern */
  .card--pattern { left: 17px; top: 9px; width: 567px; height: 326px; }
  .card--pattern .services { right: 18px; top: 8px; color: var(--white); }
  .card--pattern .wordmark { left: 150px; top: 108px; font-size: 58px; }

  /* Standalone logo */
  .logo-solo { left: 703px; top: 150px; font-size: 66px; color: var(--ink-blue); }

  /* Card back – contact */
  .card--contact { left: 17px; top: 526px; width: 554px; height: 328px; }
  .card--contact .wordmark { left: 28px; top: 110px; font-size: 54px; }
  .person { position: absolute; right: 16px; top: 30px; text-align: center; color: var(--white); width: 250px; }
  .person .name { font-family: "Lobster", cursive; font-size: 32px; line-height: 1; }
  .person .role { font-family: "Lobster", cursive; font-size: 16px; margin-top: 2px; }
  .contact {
    position: absolute; right: 16px; bottom: 20px; text-align: right;
    font-family: "Tinos", "Times New Roman", serif; font-weight: 700;
    font-size: 14px; line-height: 1.3; color: var(--white);
  }

  /* Card alternate front */
  .card--soft { left: 625px; top: 526px; width: 545px; height: 322px; }
  .card--soft .wordmark { left: 50px; top: 110px; font-size: 54px; }
  .card--soft .services { right: 8px; top: 24px; color: var(--service-green); text-align: center; font-size: 16px; }
</style>
</head>
<body>
<main class="canvas">

  <section class="card card--pattern">
    <svg class="bg" viewBox="0 0 567 326" preserveAspectRatio="none" aria-hidden="true">
      <rect width="567" height="326" fill="var(--brick)"/>
      <polygon points="0,0 160,0 80,80" fill="var(--lemon)"/>
      <polygon points="0,0 80,80 0,165" fill="var(--leaf)"/>
      <polygon points="0,165 150,326 0,326" fill="var(--leaf)"/>
      <polygon points="330,0 567,0 567,210" fill="var(--leaf)"/>
      <polygon points="567,210 567,326 360,326 460,240" fill="var(--lemon)"/>
      <polygon points="160,0 330,0 245,80" fill="var(--brick-dark)" opacity=".5"/>
      <g stroke="var(--brick-dark)" stroke-width="4" fill="none" opacity=".8">
        <line x1="0" y1="165" x2="245" y2="-20"/>
        <line x1="60" y1="0" x2="520" y2="326"/>
        <line x1="300" y1="326" x2="567" y2="110"/>
      </g>
    </svg>
    <div class="services">Interior Decorating<br>Property Styling<br>Colour Consulting</div>
    <div class="wordmark"><span class="dot"></span><span>Velvet<br>Lantern</span></div>
  </section>

  <div class="wordmark logo-solo"><span class="dot"></span><span>Velvet<br>Lantern</span></div>

  <section class="card card--contact">
    <svg class="bg" viewBox="0 0 554 328" preserveAspectRatio="none" aria-hidden="true">
      <defs>
        <linearGradient id="paleFade" x1="0" y1="0" x2="0" y2="1">
          <stop offset="0" stop-color="var(--leaf-pale)"/>
          <stop offset=".6" stop-color="#a6c496"/>
          <stop offset="1" stop-color="#6f9466"/>
        </linearGradient>
      </defs>
      <rect width="554" height="328" fill="var(--leaf)"/>
      <polygon points="0,0 264,0 376,166 222,328 0,328" fill="var(--white)"/>
      <polygon points="0,0 256,0 366,166 214,328 0,328" fill="url(#paleFade)"/>
    </svg>
    <div class="person">
      <div class="name">Maeve Hollis</div>
      <div class="role">Director</div>
    </div>
    <div class="contact">
      Mobile: 0427 386 509<br>
      Email: maeve@velvetlantern.com.au<br>
      Web: www.velvetlantern.com.au
    </div>
    <div class="wordmark"><span class="dot"></span><span>Velvet<br>Lantern</span></div>
  </section>

  <section class="card card--soft">
    <svg class="bg" viewBox="0 0 545 322" preserveAspectRatio="none" aria-hidden="true">
      <defs>
        <linearGradient id="steelFade" x1="0" y1="0" x2="1" y2="1">
          <stop offset="0" stop-color="#c9cccd"/>
          <stop offset="1" stop-color="var(--steel)"/>
        </linearGradient>
        <linearGradient id="creamFade" x1="0" y1="0" x2="0" y2="1">
          <stop offset="0" stop-color="var(--cream)"/>
          <stop offset="1" stop-color="var(--olive)"/>
        </linearGradient>
      </defs>
      <rect width="545" height="322" fill="url(#steelFade)"/>
      <path d="M0,0 H140 C120,30 70,40 40,40 C20,40 10,60 0,80 Z" fill="var(--leaf-dark)"/>
      <path d="M40,60 C80,25 280,20 340,60 C380,90 370,230 330,280 C290,315 90,315 50,280 C10,240 10,100 40,60 Z" fill="#f4f4f2"/>
      <path d="M405,15 C390,18 380,40 380,80 C380,150 385,230 400,250 H545 V15 Z" fill="url(#creamFade)"/>
    </svg>
    <div class="services">Interior Decorating<br>Property Styling<br>Colour Consulting</div>
    <div class="wordmark" style="color: var(--lemon);"><span class="dot"></span><span style="color: var(--lemon);">Velvet<br>Lantern</span></div>
  </section>

</main>
</body>
</html>
```